Wordpress Design Project - QuorvanLabs

I would like our existing old website at www.quorvanlabs.example to be redesigned to a more modern attractive site using Wordpress, a total of 5 web pages. And also installed onto our new web hosting site. Please visit the existing website using Microsoft Internet explorer to see the content.
The new site must be compatible with all popular web browsers and mobile devices (if possible).
There should be a contact button available on each page with an associated form in case an interested person wants to contact us. This form must be spam proof not allowing automated crawlers from activating it.
Updates

There are only 5 pages web pages to this QuorvanLabs project.

Industry/Entity Type

Internet

```html
<!DOCTYPE html>
<html lang="en">
<head>
<meta charset="utf-8">
<title>QuorvanLabs</title>
<link rel="stylesheet" href="https://fonts.googleapis.com/css2?family=Oswald:wght@500;600&family=Open+Sans:wght@400;600;700&family=Arimo:wght@400;700&display=swap">
<style>
:root{
  --blue-dark:#0d3a7a;
  --blue:#1f4fa0;
  --blue-mid:#2a63b8;
  --blue-bright:#1a8fd8;
  --sky:#2aa3e6;
  --orange:#f0a01a;
  --orange-dark:#c97a06;
  --text:#333;
  --white:#fff;
  --form-blue:#2f7fc6;
}
*{box-sizing:border-box;margin:0;padding:0}
html,body{width:762px;height:1200px;overflow:hidden;background:#f4f4f4;font-family:"Open Sans",Arial,sans-serif;color:var(--text)}
.page{position:absolute;left:26px;top:12px;width:710px;height:1180px;background:var(--white);box-shadow:0 0 4px rgba(0,0,0,.35)}
.abs{position:absolute}

/* header */
.brand{left:16px;top:30px;display:flex;align-items:center;gap:10px}
.brand-dot{width:42px;height:42px;border-radius:50%;background:var(--blue)}
.brand-name{font-family:Arimo,Arial,sans-serif;font-weight:700;font-size:25px;color:var(--blue)}
.brand-tag{left:68px;top:66px;font-size:6.5px;color:var(--blue-dark);font-weight:700}
.support{right:16px;top:14px;text-align:center;width:150px}
.support-pill{background:linear-gradient(var(--blue-mid),var(--blue-dark));color:#fff;border-radius:16px;height:31px;line-height:27px;font-family:Arimo,Arial,sans-serif;font-style:italic;font-weight:700;font-size:13px;border:2px solid #0a2d60}
.support-pill b{font-size:20px}
.toll{font-family:Arimo,Arial,sans-serif;font-style:italic;font-weight:700;font-size:14px;color:#111;margin-top:5px;line-height:15px}
.toll span{display:block;color:var(--blue)}

/* nav */
.nav{left:16px;top:108px;width:678px;height:30px;background:linear-gradient(var(--blue-mid),var(--blue-dark));display:flex;align-items:center;border:1px solid #0a2d60}
.nav a{color:#fff;text-decoration:none;font-size:9.5px;font-weight:600;text-transform:uppercase;flex:1;text-align:center;height:100%;line-height:28px;white-space:nowrap}
.nav a.active{background:linear-gradient(#f7b733,var(--orange-dark));flex:0 0 80px}

/* hero */
.hero{left:18px;top:148px;width:674px;height:276px;border:3px solid #fff;box-shadow:0 0 3px rgba(0,0,0,.4);overflow:hidden}
.hero-photo{position:absolute;inset:0;background:linear-gradient(120deg,#2a5aa8 0%,#15428a 50%,#0d3a7a 100%)}
.hero-title{right:36px;top:100px;font-family:Oswald,Arial,sans-serif;font-weight:500;color:#fff;font-size:31px;line-height:40px;text-align:left}
.hero-arrow{top:126px;width:18px;height:20px;background:var(--blue-mid);border:1px solid #fff;display:flex;align-items:center;justify-content:center}
.dots{left:272px;top:247px;width:130px;height:26px;background:var(--blue-dark);clip-path:polygon(10% 0,90% 0,100% 100%,0 100%);display:flex;justify-content:center;align-items:center;gap:5px;padding-top:2px}
.dots i{width:9px;height:9px;border-radius:50%;background:#fff;display:block}
.dots i.on{background:#222;border:1px solid #fff}

/* intro */
.intro{left:20px;top:448px;width:436px;font-size:8.8px;line-height:12.6px;color:#444}
.intro h2{font-family:Arial,sans-serif;font-weight:400;font-size:13px;color:#222;margin-bottom:9px}
.intro h2 span{font-size:17px;color:var(--blue-bright)}
.intro p{margin-bottom:12px}
.intro a{color:var(--blue-bright);font-weight:700;text-decoration:none}
.intro h2.why{margin-top:16px}

/* quote form */
.quote{left:464px;top:445px;width:228px;height:310px;background:var(--form-blue);border-radius:18px;border:3px solid #1b5f9e;padding:52px 14px 0}
.quote-head{left:6px;top:6px;width:210px;height:36px;border-radius:18px;background:linear-gradient(#fbc44a,var(--orange-dark));display:flex;align-items:center;gap:10px;padding-left:12px;font-family:Oswald,Arial,sans-serif;font-weight:600;font-size:15px;color:#3b2a07}
.field{background:#fff;border-radius:6px;height:26px;margin-bottom:6px;font-size:8px;color:#999;padding:8px 10px}
.field.tall{height:60px}
.captcha{background:#fff;border-radius:6px;height:46px;padding:6px;display:flex;align-items:center;gap:5px}
.captcha-img{width:118px;height:32px;background:linear-gradient(90deg,#e8e8e8,#f6f6f6)}
.captcha-btns{display:flex;flex-direction:column;gap:1px}
.captcha-btns i{width:10px;height:10px;background:var(--blue-mid);display:block}
.captcha-badge{width:40px;height:26px;border-radius:50%;background:#e0e0e0}
.submit{margin-top:10px;width:75px;height:27px;border-radius:7px;background:linear-gradient(#f7b733,var(--orange-dark));border:1px solid #8a5200;color:#2a1c00;font-weight:700;font-size:9.5px;text-align:center;line-height:25px}

/* services */
.services{left:16px;top:783px;width:678px;height:242px;background:linear-gradient(#f6f6f6,#e4e4e4)}
.services-title{left:0;top:5px;width:100%;text-align:center;font-family:Arial,sans-serif;font-weight:700;font-size:11px;color:#444}
.services-title::before,.services-title::after{content:"";display:inline-block;width:256px;height:4px;background:#d6d6d6;vertical-align:middle;margin:0 8px}
.card{top:46px;width:188px;height:176px;background:#fff;box-shadow:0 3px 4px rgba(0,0,0,.15)}
.card h3{height:36px;line-height:36px;text-align:center;background:linear-gradient(#fff,#ececec);font-family:Oswald,Arial,sans-serif;font-weight:500;font-size:12px;color:#222;text-transform:uppercase}
.card-photo{margin:10px 10px 0;height:66px;border:1px solid #ddd}
.card p{margin:14px 10px 0;font-size:8.6px;line-height:12px;color:#222}
.card a{display:block;margin:8px 10px 0;font-size:7.5px;color:var(--blue-mid);text-decoration:none}

/* footer */
.footer{left:16px;top:1038px;width:678px;height:130px;background:linear-gradient(var(--sky),#1a7fcc);color:#fff}
.footer-address{left:10px;top:18px;font-size:8.8px;line-height:13px;font-style:normal}
.footer-map{left:230px;top:12px;width:240px;height:72px;border:2px solid #1b5f9e;background:linear-gradient(135deg,#cfe0ee,#e7dcc0 55%,#b9d3e8)}
.social{left:535px;top:16px;text-align:center;font-size:8.5px;width:90px}
.social-row{display:flex;justify-content:center;gap:12px;margin-top:12px}
.social-row i{width:22px;height:22px;border-radius:50%;background:#fff;display:block;opacity:.9}
.footer-bar{left:0;top:96px;width:100%;height:34px;border-top:1px solid rgba(255,255,255,.35);font-size:7.5px;display:flex;align-items:center;padding:0 20px}
.footer-bar .links{margin-left:144px}
</style>
</head>
<body>
<div class="page">
  <header>
    <div class="abs brand"><span class="brand-dot"></span><span class="brand-name">QuorvanLabs</span></div>
    <div class="abs brand-tag">A Leading Edge Technology Company</div>
    <div class="abs support">
      <div class="support-pill"><b>24x7</b> SUPPORT</div>
      <div class="toll">TOLL FREE NO:<span>(900) 5550 1427</span></div>
    </div>
  </header>

  <nav class="abs nav">
    <a class="active" href="#">Home</a>
    <a href="#">Support Services</a>
    <a href="#">Telephoone VoIP Solutions</a>
    <a href="#">IP, LAN &amp; Internet</a>
    <a href="#">Contact</a>
  </nav>

  <section class="abs hero">
    <div class="hero-photo" role="img" aria-label="Photo of a businessman with a laptop under an open sky"></div>
    <h1 class="abs hero-title">WIRED/WIRELESS<br>INTERNET/INTRANET</h1>
    <div class="abs hero-arrow" style="left:2px"><svg width="8" height="10"><path d="M7 0 L1 5 L7 10Z" fill="#fff"/></svg></div>
    <div class="abs hero-arrow" style="right:2px"><svg width="8" height="10"><path d="M1 0 L7 5 L1 10Z" fill="#fff"/></svg></div>
    <div class="abs dots"><i class="on"></i><i></i><i></i><i></i><i></i><i></i></div>
  </section>

  <section class="abs intro">
    <h2>welcome to <span>QuorvanLabs</span></h2>
    <p>QuorvanLabs provides complete telephone VoIP PBX solutions for businesses large and small.</p>
    <p>Our team of telecom engineers will design and install the best business telephone VoIP PBX solution for your requirements.&nbsp; System features include: standard and advanced PBX call control actions, video telephone calling, toll free calling any where in the world, and 24x7 support.<br>For more details, <a href="#">click here</a></p>
    <p>We also provide complete wired and wireless LAN/WAN/IP solutions and services for data, voice, Internet and private intranet networks to a variety of industries, including hospitality, industrial, commercial and institutional groups.Our Support Services Division call center provides 24 x 7 help desk technical support services for industries including telecommunications, commercial and lodging / hotel.</p>
    <h2 class="why">why <span>QuorvanLabs?</span></h2>
    <p>QuorvanLabs provides state of the art VoIP PBX phone solutions with products tailored to small, medium, and large businesses. Our engineering team will asses your communication requirements and provide you with the best designed solution for your business needs.</p>
    <p>QuorvanLabs will be there for you during the whole process. From the initial quote all the way through installation and support. QuorvanLabs is committed to you!</p>
  </section>

  <form class="abs quote">
    <div class="abs quote-head">
      <svg width="26" height="18" viewBox="0 0 26 18"><rect x="1" y="1" width="24" height="16" fill="#3a86c8" stroke="#1b5f9e"/><path d="M1 1 L13 10 L25 1" fill="none" stroke="#fff" stroke-width="1.5"/></svg>
      GET A FREE QUOTE
    </div>
    <div class="field">Your Name</div>
    <div class="field">Your Phone No</div>
    <div class="field">Your Email Id</div>
    <div class="field tall">Your Message or Queries</div>
    <div class="captcha">
      <div class="captcha-img" role="img" aria-label="Security check word"></div>
      <div class="captcha-btns"><i></i><i></i><i></i></div>
      <div class="captcha-badge"></div>
    </div>
    <div class="submit">SUBMIT</div>
  </form>

  <section class="abs services">
    <h2 class="abs services-title">OUR SERVICES</h2>
    <article class="abs card" style="left:10px">
      <h3>Telephone VoIP Solutions</h3>
      <div class="card-photo" role="img" aria-label="Rack mounted VoIP telephony hardware" style="background:linear-gradient(#2a2a2e,#111)"></div>
      <p>Lorem ipsum dolor sit maer seta di mari a nuno valencia est do dummy text</p>
      <a href="#">» Read More</a>
    </article>
    <article class="abs card" style="left:245px">
      <h3>IP, LAN &amp; Internet</h3>
      <div class="card-photo" role="img" aria-label="Assorted network and power cables" style="background:linear-gradient(#f4f4f4,#c9c9c9)"></div>
      <p>Lorem ipsum dolor sit maer seta di mari a nuno valencia est do dummy text</p>
      <a href="#">» Read More</a>
    </article>
    <article class="abs card" style="left:480px">
      <h3>24x7 Help/Support</h3>
      <div class="card-photo" role="img" aria-label="Help desk staff wearing headsets" style="background:linear-gradient(90deg,#d8cfc6,#f2f2f2)"></div>
      <p>Lorem ipsum dolor sit maer seta di mari a nuno valencia est do dummy text</p>
      <a href="#">» Read More</a>
    </article>
  </section>

  <footer class="abs footer">
    <address class="abs footer-address">Quorvan Labs<br>Larkmoor Lane, Eastfield, EF4 2QX<br>Email: hello@quorvanlabs.example<br>Phone: 01632 960418</address>
    <div class="abs footer-map" role="img" aria-label="Location map"></div>
    <div class="abs social">Get In Touch With Us
      <div class="social-row"><i aria-label="Social profile"></i><i aria-label="Social profile"></i><i aria-label="Social profile"></i></div>
    </div>
    <div class="abs footer-bar">
      <span>© 2013, All Rights Reserved</span>
      <span class="links">Terms &amp; Conditions &nbsp;|&nbsp; Privacy &nbsp;|&nbsp; Help</span>
    </div>
  </footer>
</div>
</body>
</html>
```